Painting Contractor Business Card Design

We are looking for a cool, bold, modern, polished, business card design. We are a high-end residential painting contractor. Please incorporate our logo and keep with our green/black color scheme. We are interested in seeing 2-sided and 1-sided options. Thank you very much!

Industry/Entity Type

Business

Contact Information for Business Card

Info for the card:
Owen Talsky
mobile 206-555-0193
email owen@kestrowfinish.net
web www.kestrowfinish.net

```html
<!DOCTYPE html>
<html lang="en">
<head>
<meta charset="utf-8">
<title>Kestrow Finish – Business Card</title>
<link rel="stylesheet" href="https://fonts.googleapis.com/css2?family=Mulish:wght@400;700;800&display=swap">
<style>
  :root {
    --stage: #e9e9e7;
    --card-white: #ffffff;
    --card-black: #0c0c0c;
    --card-black-soft: #1c1c1c;
    --ink: #1b1b1b;
    --ink-soft: #444444;
    --rule: #8a8a8a;
    --brand-green: #3aa84a;
    --accent-teal: #2bb3a0;
    --accent-lime: #9ccc3a;
    --accent-yellow: #f2b31c;
    --accent-orange: #e8561f;
  }
  * { margin: 0; padding: 0; box-sizing: border-box; }
  html, body { width: 1200px; height: 873px; overflow: hidden; }
  body {
    background: var(--stage);
    font-family: "Mulish", sans-serif;
    position: relative;
  }
  .card {
    position: absolute;
    top: 286px;
    width: 520px;
    height: 288px;
    box-shadow: 0 10px 28px rgba(0,0,0,.22);
    overflow: hidden;
  }

  /* Back side */
  .card--back { left: 50px; background: var(--card-black); }
  .card--back .texture {
    position: absolute;
    inset: 0;
    background: linear-gradient(135deg, var(--card-black-soft) 0%, var(--card-black) 55%, var(--card-black-soft) 100%);
  }
  .card--back .brand-block {
    position: absolute;
    left: 296px;
    top: 62px;
    width: 250px;
    height: 250px;
    background: var(--brand-green);
  }
  .card--back .web {
    position: absolute;
    left: 64px;
    top: 136px;
    font-size: 12px;
    font-weight: 700;
    color: var(--card-white);
    letter-spacing: .2px;
  }
  .card--back .web .green { color: var(--brand-green); }

  /* Front side */
  .card--front { left: 630px; background: var(--card-white); }
  .accent-chips { position: absolute; top: 0; right: 0; }
  .wordmark {
    position: absolute;
    left: 58px;
    top: 62px;
    display: flex;
    align-items: center;
    gap: 10px;
  }
  .wordmark__square {
    width: 22px; height: 22px;
    background: var(--brand-green);
  }
  .wordmark__name {
    font-size: 23px;
    font-weight: 800;
    letter-spacing: .3px;
    color: var(--ink);
  }
  .holder {
    position: absolute;
    right: 40px;
    top: 154px;
    text-align: right;
    font-size: 17px;
    font-weight: 800;
    color: var(--ink);
  }
  .holder__underline {
    position: absolute;
    right: 40px;
    top: 182px;
    width: 460px;
    height: 1px;
    background: var(--rule);
  }
  .holder__underline::after {
    content: "";
    position: absolute;
    right: 0;
    top: 2px;
    width: 40px;
    height: 2px;
    background: var(--brand-green);
  }
  .contact {
    position: absolute;
    right: 40px;
    top: 194px;
    text-align: right;
    font-size: 11.5px;
    line-height: 15px;
    color: var(--ink-soft);
    font-style: normal;
  }
  .contact__web { font-weight: 800; color: var(--ink); }
  .contact__web .green { color: var(--brand-green); }
</style>
</head>
<body>
  <section class="card card--back" aria-label="Card back">
    <div class="texture" role="img" aria-label="Dark faceted line pattern"></div>
    <div class="brand-block" aria-hidden="true"></div>
    <p class="web">www.KestrowFinish<span class="green">.net</span></p>
  </section>

  <section class="card card--front" aria-label="Card front">
    <svg class="accent-chips" width="150" height="24" viewBox="0 0 150 24" aria-hidden="true">
      <defs>
        <linearGradient id="chipGreen" x1="0" y1="0" x2="1" y2="1">
          <stop offset="0" stop-color="var(--accent-teal)"/>
          <stop offset="1" stop-color="var(--accent-lime)"/>
        </linearGradient>
      </defs>
      <rect x="2" y="0" width="22" height="22" fill="url(#chipGreen)"/>
      <rect x="66" y="0" width="22" height="22" fill="var(--accent-yellow)"/>
      <rect x="122" y="0" width="14" height="22" fill="var(--accent-orange)"/>
    </svg>

    <div class="wordmark">
      <span class="wordmark__square" aria-hidden="true"></span>
      <span class="wordmark__name">KESTROWFINISH</span>
    </div>

    <p class="holder">Owen Talsky</p>
    <div class="holder__underline" aria-hidden="true"></div>

    <address class="contact">
      <div>206 555 0193</div>
      <div>owen@kestrowfinish.net</div>
      <div class="contact__web">www.<span class="green">kestrowfinish</span>.net</div>
    </address>
  </section>
</body>
</html>
```